Brindle Tavern & Lodge Supplies need a website

We need a website designed and created to facilitate us to promote & sell our products online. We buy excess / clearance lots of pub, cafe, restaurant & hotel furniture and equipment (usually from businesses that have excess inventory after a refurb or have closed down). We then sell these to other businesses mainly through our Chatterly page "Brindle Tavern & Lodge Supplies" but the process is cumbersome for the following reasons:
1) We dont have a stock list and images as it changes daily and people can only rely on recent posts and dont know if something is for sale still or is sold
2) we do not have the facility to sell online.

We are open to ideas and design concepts

We already have a logo & stationery deisgned

its probably best to look through our Chatterly page to better understand what we do

We would consider a catalogue / by department / category user interface such as:
https://brambleworth-trade-fittings.co.uk/

Our preference would be to change / delete / update stock via smartphone to best facilitate the maintenance of the website which i will do myself

Suggested categories would include:
Bar Furniture
Bar Equipment
Restaurant Furniture
Catering Equipment
Bedroom Furniture
Miscellaneous

Sub categories would include:
Bar Furniture:
Bar Stools
Bar Tables
Benches
Tub chairs
Arm chairs
Pub Mirrors
Pub Signs
Pub Memorabilia

Bar Equipment:
Bottle Coolers
Ice Machines
Glass Washers
Tills
Lighting
Sound
Wireless waiter
Glassware
Taps
Line coolers
Snooker tables
Pool tables
gaming machines

Restaurant Furniture:
Tables
Chairs
Wine racks
Dressers
Couches
Bench seating
Tub Chairs
Arm chairs
High chairs
Menu boards
Mirrors
Pictures

Catering Equipment:
Fridges
Freezers
Ovens
Cookers
Fryers
Carvery units
Hot display units
Refrigerated displays
Sinks
Stainless steel units
Microwaves
Mixers
Crockery
Cutlery
Utensils
Glassware

Bedroom Furniture:
Beds
Headboards
Wardrobes
Lockers
Dressing Tables
Mirrors
Lamps
Pictures

Profit sharing schemes:
Pool Tables
Juke Boxes
Gaming Machines

Target Market(s)

Pubs
Restaurants
cafes
guest houses
hotels

Industry/Entity Type

Hospitality

Number of Pages Required

5+ page

Colors

Designer to choose colors to be used in the design.

Requirements
Must have
• Website featuring our categories of stock to sell
Nice to have
• Ecommerce option
Should not have
• just a front page

```html
<!DOCTYPE html>
<html lang="en">
<head>
<meta charset="utf-8">
<title>Brindle Tavern &amp; Lodge Supplies</title>
<link href="https://fonts.googleapis.com/css2?family=Oswald:wght@400;500;600&family=Roboto:wght@400;500;700&display=swap" rel="stylesheet">
<style>
:root{
  --red:#b3121d;
  --red-dark:#8f0d16;
  --ink:#1c1c1c;
  --text:#555;
  --muted:#888;
  --line:#e3e3e3;
  --paper:#ffffff;
  --soft:#f3f3f3;
  --footer:#1b1b1b;
}
*{box-sizing:border-box;margin:0;padding:0}
html,body{width:1200px;height:3500px;overflow:hidden}
body{font-family:"Roboto",Arial,sans-serif;color:var(--text);background:var(--paper);font-size:14px;line-height:1.6}
h1,h2,h3,h4{font-family:"Oswald",Arial,sans-serif;font-weight:500;color:var(--ink)}
.btn{display:inline-block;font-family:"Oswald",Arial,sans-serif;font-size:14px;line-height:20px;padding:8px 24px;background:var(--ink);color:#fff;letter-spacing:.5px}
.btn-outline{border:1px solid #fff}
.btn-red{background:var(--red)}

/* header */
.site-header{height:70px;display:flex;align-items:center;justify-content:space-between;padding:0 60px;border-bottom:1px solid var(--line)}
.brand{display:flex;align-items:center;gap:10px}
.brand-mark{width:22px;height:22px;background:var(--red)}
.brand-name{font-family:"Roboto",sans-serif;font-weight:700;font-size:15px;color:var(--ink)}
.main-nav{display:flex;height:70px}
.main-nav a{display:flex;align-items:center;padding:0 26px;font-family:"Oswald",sans-serif;font-size:15px;color:var(--ink)}
.main-nav a.active{background:var(--red);color:#fff}

/* hero */
.hero{position:relative;height:540px;background:linear-gradient(160deg,#6d5a48 0%,#3b302a 45%,#1f1a17 100%);text-align:center;color:#fff;overflow:hidden}
.hero-shade{position:absolute;inset:0;background:rgba(0,0,0,.35)}
.hero-copy{position:relative;padding-top:90px}
.hero-title{font-family:"Oswald",sans-serif;font-size:72px;font-weight:600;color:#fff;letter-spacing:3px;line-height:1}
.hero-sub{font-family:"Oswald",sans-serif;font-size:30px;line-height:1.3;color:#fff;margin:18px 0 28px;letter-spacing:1px}
.dots{display:flex;justify-content:center;gap:8px;margin-top:28px}
.dots span{width:8px;height:8px;border-radius:50%;background:rgba(255,255,255,.5)}
.dots span.on{background:#fff}
.hero-panels{position:absolute;left:0;right:0;bottom:0;height:150px;display:flex}
.hero-panel{flex:1;display:flex;justify-content:space-between;align-items:center;padding:0 60px;text-align:left}
.hero-panel.seller{background:rgba(20,20,20,.78)}
.hero-panel.buyer{background:rgba(179,18,29,.9)}
.hero-panel h3{color:#fff;font-size:24px;line-height:1.3}
.hero-panel p{font-size:13px;color:#eee;max-width:380px;margin:4px 0 10px;line-height:1.5}

/* categories */
.categories{height:800px;padding-top:46px;text-align:center;overflow:hidden}
.section-title{font-size:40px;font-weight:400;line-height:1.3;margin-bottom:16px}
.cat-tabs{display:flex;justify-content:center;gap:6px;margin-bottom:28px}
.cat-tabs span{font-size:13px;padding:4px 12px;color:var(--ink)}
.cat-tabs span.on{background:var(--red);color:#fff}
.cat-grid{width:1080px;margin:0 auto;display:grid;grid-template-columns:repeat(3,1fr);gap:28px 30px}
.cat-card{border:1px solid var(--line);box-shadow:0 2px 6px rgba(0,0,0,.08)}
.cat-photo{height:210px;position:relative;display:flex;flex-direction:column;align-items:center;justify-content:center;gap:12px}
.cat-photo .count{font-family:"Oswald",sans-serif;color:#fff;font-size:30px;line-height:1.2;position:relative}
.cat-photo .btn{position:relative;padding:5px 30px}
.cat-photo .veil{position:absolute;inset:0;background:rgba(0,0,0,.45)}
.cat-name{font-family:"Oswald",sans-serif;font-size:19px;line-height:26px;color:var(--ink);padding:12px 0}
.ph-bar{background:linear-gradient(135deg,#a7a29c,#5e5852)}
.ph-bareq{background:linear-gradient(135deg,#5b5fd0,#1c1f6b)}
.ph-rest{background:linear-gradient(135deg,#d7c1a6,#7b5b3c)}
.ph-cater{background:linear-gradient(135deg,#cfd2d4,#6f7478)}
.ph-bed{background:linear-gradient(135deg,#e6e1d9,#9c958a)}
.ph-pool{background:linear-gradient(135deg,#2f7d42,#13351c)}

/* about */
.about{position:relative;height:290px;background:linear-gradient(120deg,#2a1f18 0%,#5a3d22 55%,#8a6a3f 100%);padding:42px 60px;overflow:hidden}
.about-shade{position:absolute;inset:0;background:rgba(0,0,0,.45)}
.about-copy{position:relative;width:520px}
.about h2{color:#fff;font-size:40px;font-weight:400;line-height:1.3;margin-bottom:10px}
.about p{color:#ddd;font-size:13px;line-height:1.6;margin-bottom:20px}

/* testimonials */
.testimonials{height:410px;background:var(--soft);padding-top:42px;text-align:center;overflow:hidden}
.avatars{display:flex;justify-content:center;align-items:center;gap:18px;margin-bottom:-30px;position:relative;z-index:1}
.avatar{width:62px;height:62px;border-radius:50%;background:linear-gradient(135deg,#c9b3a0,#7a6656);border:3px solid #fff}
.avatar.main{width:78px;height:78px}
.quote-card{width:820px;margin:0 auto;background:#fff;padding:45px 60px 26px 110px;position:relative;text-align:left}
.quote-mark{position:absolute;left:34px;top:30px;font-family:"Oswald",serif;font-size:90px;color:#ccc;line-height:1}
.quote-card h4{text-align:center;font-size:17px;margin-bottom:8px}
.quote-card p{font-size:13px}
.testimonials .dots span{background:#ccc}
.testimonials .dots span.on{background:var(--red)}
.testimonials .dots{margin-top:20px}

/* blog */
.blog{height:960px;padding-top:46px;text-align:center;overflow:hidden}
.post{width:1080px;margin:0 auto 50px;position:relative;height:330px;text-align:left}
.post-photo{position:absolute;top:0;width:620px;height:330px}
.post-card{position:absolute;top:40px;width:520px;background:#fff;padding:24px 28px;box-shadow:0 3px 14px rgba(0,0,0,.14)}
.post.left .post-photo{left:0}
.post.left .post-card{right:0}
.post.right .post-photo{right:0}
.post.right .post-card{left:0}
.post-date{font-size:12px;color:var(--muted)}
.post-card h3{font-family:"Roboto",sans-serif;font-weight:700;font-size:17px;margin:6px 0 10px}
.post-card p{font-size:13px;line-height:1.6}
.post-foot{display:flex;justify-content:space-between;align-items:center;margin-top:14px}
.read-more{font-family:"Oswald",sans-serif;color:var(--ink);font-size:15px}
.post-meta{font-size:12px;color:var(--muted);display:flex;gap:14px}
.ph-blog1{background:linear-gradient(135deg,#d9d4cc,#6c6257)}
.ph-blog2{background:linear-gradient(135deg,#9a8f80,#2f2a25)}

/* footer */
.site-footer{height:380px;background:var(--footer);color:#bbb;padding:50px 60px 0;display:grid;grid-template-columns:1.4fr 1fr 1fr 1.5fr;gap:40px;font-size:13px}
.site-footer h4{color:#fff;font-size:16px;margin-bottom:14px}
.site-footer .brand-name{color:#fff}
.contact-list{margin-top:24px;list-style:none}
.contact-list li{margin-bottom:10px}
.contact-list b{color:#fff;font-weight:500;display:inline-block;width:74px}
.link-list{list-style:none}
.link-list li{margin-bottom:6px}
.newsletter p{margin-bottom:16px}
.newsletter .field{height:38px;background:#fff;color:#999;padding:8px 12px;margin-bottom:12px}
.bottom-bar{height:50px;background:var(--red);color:#fff;display:flex;align-items:center;justify-content:space-between;padding:0 60px;font-size:13px}
.cards{display:flex;gap:8px}
.cards span{width:38px;height:24px;background:#fff;border-radius:3px}
</style>
</head>
<body>

<header class="site-header">
  <div class="brand"><span class="brand-mark"></span><span class="brand-name">Brindle Tavern &amp; Lodge Supplies</span></div>
  <nav class="main-nav">
    <a class="active">Home</a><a>About Us</a><a>Categories</a><a>Blog</a><a>Testimonial</a><a>Contact Us</a>
  </nav>
</header>

<section class="hero" role="img" aria-label="Photo of a furnished pub and restaurant interior">
  <div class="hero-shade"></div>
  <div class="hero-copy">
    <h1 class="hero-title">BUY &amp; SELL</h1>
    <p class="hero-sub">Pub, Cafe, Restaurant &amp; Hotel Furniture and Equipment</p>
    <a class="btn">Shop Now</a>
    <div class="dots"><span class="on"></span><span></span><span></span></div>
  </div>
  <div class="hero-panels">
    <div class="hero-panel seller">
      <div>
        <h3>We Are Seller</h3>
        <p>Lorem Ipsum is simply dummy text of the printing and typesetting industry. Lorem Ipsum has been the industry's standard dummy.</p>
        <a class="btn">Read More</a>
      </div>
      <svg width="56" height="56" viewBox="0 0 56 56" fill="none" stroke="#fff" stroke-width="2.5"><path d="M10 28 L22 16 H46 V40 H22 Z"/><circle cx="38" cy="28" r="3"/></svg>
    </div>
    <div class="hero-panel buyer">
      <div>
        <h3>We Are Buyer</h3>
        <p>Lorem Ipsum is simply dummy text of the printing and typesetting industry. Lorem Ipsum has been the industry's standard dummy.</p>
        <a class="btn">Read More</a>
      </div>
      <svg width="56" height="56" viewBox="0 0 56 56" fill="none" stroke="#fff" stroke-width="2.5"><path d="M8 14 H16 L22 38 H44 L48 20 H19"/><circle cx="25" cy="45" r="3"/><circle cx="41" cy="45" r="3"/></svg>
    </div>
  </div>
</section>

<section class="categories">
  <h2 class="section-title">Our Categories</h2>
  <div class="cat-tabs">
    <span class="on">All</span><span>Bar Furniture</span><span>Bar Equipment</span><span>Restaurant Furniture</span><span>Catering Equipment</span><span>Bedroom Furniture</span><span>Profit sharing schemes</span>
  </div>
  <div class="cat-grid">
    <div class="cat-card">
      <div class="cat-photo ph-bar" role="img" aria-label="Photo of bar stools and bar counter">
        <div class="veil"></div><span class="count">8 Items</span><a class="btn">View</a>
      </div>
      <div class="cat-name">Bar Furniture</div>
    </div>
    <div class="cat-card"><div class="cat-photo ph-bareq" role="img" aria-label="Photo of a lit bar with equipment"></div><div class="cat-name">Bar Equipment</div></div>
    <div class="cat-card"><div class="cat-photo ph-rest" role="img" aria-label="Photo of restaurant tables and chairs"></div><div class="cat-name">Restaurant Furniture</div></div>
    <div class="cat-card"><div class="cat-photo ph-cater" role="img" aria-label="Photo of a stainless steel commercial kitchen"></div><div class="cat-name">Catering Equipment</div></div>
    <div class="cat-card"><div class="cat-photo ph-bed" role="img" aria-label="Photo of a hotel bedroom"></div><div class="cat-name">Bedroom Furniture</div></div>
    <div class="cat-card"><div class="cat-photo ph-pool" role="img" aria-label="Photo of a pool table"></div><div class="cat-name">Profit sharing schemes</div></div>
  </div>
</section>

<section class="about" role="img" aria-label="Photo of a warmly lit restaurant dining room">
  <div class="about-shade"></div>
  <div class="about-copy">
    <h2>About Us</h2>
    <p>Lorem Ipsum is simply dummy text of the printing and typesetting industry. Lorem Ipsum has been the industry's standard dummy text ever since the 1500s, when an unknown printer took a galley of type and scrambled it to make a type specimen book. It has survived not only five centuries of Lorem Ipsum.</p>
    <a class="btn btn-outline">Read More</a>
  </div>
</section>

<section class="testimonials">
  <h2 class="section-title">What Customer Saying</h2>
  <div class="avatars">
    <span class="avatar" role="img" aria-label="Customer portrait"></span>
    <span class="avatar main" role="img" aria-label="Customer portrait"></span>
    <span class="avatar" role="img" aria-label="Customer portrait"></span>
  </div>
  <div class="quote-card">
    <span class="quote-mark">&ldquo;</span>
    <h4>John Doe</h4>
    <p>Lorem Ipsum is simply dummy text of the printing and typesetting industry. Lorem Ipsum has been the industry's standard dummy text ever since the 1500s, when an unknown printer took a galley of type and scrambled it to make a type specimen book. It has survived not only five centuries, but also the leap into electronic typesetting, remaining essentially unchanged.</p>
  </div>
  <div class="dots"><span></span><span class="on"></span><span></span></div>
</section>

<section class="blog">
  <h2 class="section-title">Recent blog Post</h2>
  <article class="post left">
    <div class="post-photo ph-blog1" role="img" aria-label="Photo of a bar counter with stools"></div>
    <div class="post-card">
      <span class="post-date">14 March 2018</span>
      <h3>Lorem Ipsum is simply dummy text of</h3>
      <p>The printing and typesetting industry. Lorem Ipsum has been the industry's standard dummy text ever since the 1500s, when an unknown printer took a galley of type and scrambled it to make a type specimen book. The printing and typesetting industry.</p>
      <div class="post-foot"><span class="read-more">Read More</span><span class="post-meta"><span>John Abott</span><span>20 Likes</span><span>10 Comments</span></span></div>
    </div>
  </article>
  <article class="post right">
    <div class="post-photo ph-blog2" role="img" aria-label="Photo of outdoor cafe tables and chairs"></div>
    <div class="post-card">
      <span class="post-date">14 March 2018</span>
      <h3>Lorem Ipsum is simply dummy text of</h3>
      <p>The printing and typesetting industry. Lorem Ipsum has been the industry's standard dummy text ever since the 1500s, when an unknown printer took a galley of type and scrambled it to make a type specimen book. The printing and typesetting industry.</p>
      <div class="post-foot"><span class="read-more">Read More</span><span class="post-meta"><span>John Abott</span><span>20 Likes</span><span>10 Comments</span></span></div>
    </div>
  </article>
  <a class="btn">View More</a>
</section>

<footer class="site-footer">
  <div>
    <div class="brand"><span class="brand-mark"></span><span class="brand-name">Brindle Tavern &amp; Lodge Supplies</span></div>
    <ul class="contact-list">
      <li><b>Address :</b>14 Hollin Lane, Marlbeck</li>
      <li><b>Cell Phone :</b>+44 1632 960 418</li>
      <li><b>E-mail :</b>hello@brindletavern.co.uk</li>
    </ul>
  </div>
  <div>
    <h4>Quick Links</h4>
    <ul class="link-list"><li>Home</li><li>About Us</li><li>Categories</li><li>Blog</li><li>Testimonial</li><li>Contact Us</li></ul>
  </div>
  <div>
    <h4>Useful Links</h4>
    <ul class="link-list"><li>New Products</li><li>Top Sellers</li><li>Manufacturers</li><li>Suppliers</li><li>Specials</li></ul>
  </div>
  <div class="newsletter">
    <h4>EMAIL NEWSLETTERS</h4>
    <p>The printing and typesetting industry. Lorem Ipsum has been the industry's standard dummy text ever since the.</p>
    <div class="field">Your Email Id</div>
    <a class="btn btn-red">Subscribe</a>
  </div>
</footer>
<div class="bottom-bar">
  <span>Copyright &copy; 2018 Brindle Tavern &amp; Lodge Supplies. All Right Reserved.</span>
  <span class="cards"><span></span><span></span><span></span><span></span></span>
</div>

</body>
</html>
```